No Credit Score TQ and KSV

I'm looking for a banner to display on emails as well as facebook. The facebook banner would need to be square and the other size is 728 x 90. We are a mortgage company that does mostly Military home loans. We would like to start out with just this banner, then do about 20 others once we find the right designer. I need something simple but that stands out. Our company website is www.harborpeakloans.com. The text for this will be ( Ask about our "No Credit Score" program for KSV and TQ)

```html
<!DOCTYPE html>
<html lang="en">
<head>
<meta charset="UTF-8">
<title>Harbor Peak Loans – No Credit Score Banner</title>
<link href="https://fonts.googleapis.com/css2?family=Cinzel:wght@600&family=Architects+Daughter&display=swap" rel="stylesheet">
<style>
  :root {
    --panel-grey: #4b4b4c;
    --brand-green: #66a02c;
    --green-light: #8cc043;
    --white: #ffffff;
    --photo-sky: #cfe4f2;
    --photo-house: #e9ecee;
    --photo-shade: #6f8292;
  }
  html, body {
    margin: 0;
    padding: 0;
    overflow: hidden;
    background: var(--white);
  }
  .banner {
    position: relative;
    width: 1200px;
    height: 148px;
    overflow: hidden;
    background: var(--white);
  }
  .banner__shapes {
    position: absolute;
    inset: 0;
  }
  .brand {
    position: absolute;
    left: 28px;
    top: 0;
    height: 148px;
    display: flex;
    align-items: center;
    gap: 16px;
  }
  .brand__mark {
    width: 40px;
    height: 40px;
    border-radius: 50%;
    background: var(--white);
    flex: none;
  }
  .brand__name {
    font-family: "Cinzel", serif;
    font-weight: 600;
    color: var(--white);
    line-height: 1;
  }
  .brand__name-main {
    display: block;
    font-size: 34px;
    letter-spacing: 2px;
  }
  .brand__name-sub {
    display: block;
    font-size: 15px;
    letter-spacing: 3px;
    margin-top: 6px;
    text-align: center;
  }
  .offer {
    position: absolute;
    left: 905px;
    width: 295px;
    top: 0;
    height: 148px;
    display: flex;
    align-items: center;
    justify-content: center;
    text-align: center;
    font-family: "Architects Daughter", cursive;
    font-size: 19px;
    line-height: 1.25;
    text-transform: uppercase;
    color: var(--white);
  }
  .offer p { margin: 0; }
</style>
</head>
<body>
  <div class="banner">
    <svg class="banner__shapes" width="1200" height="148" viewBox="0 0 1200 148">
      <defs>
        <linearGradient id="couple-photo" x1="0" y1="0" x2="1" y2="1">
          <stop offset="0" stop-color="var(--photo-sky)"/>
          <stop offset="0.45" stop-color="var(--photo-house)"/>
          <stop offset="1" stop-color="var(--photo-shade)"/>
        </linearGradient>
      </defs>
      <polygon class="hero-photo" role="img"
        aria-label="Photo of a couple embracing in front of a modern two-storey home"
        points="425,0 910,0 870,148 405,148" fill="url(#couple-photo)"/>
      <polygon class="brand-panel" points="0,0 440,0 420,148 0,148" fill="var(--panel-grey)"/>
      <polygon class="offer-panel__edge" points="895,0 912,0 872,148 855,148" fill="var(--green-light)"/>
      <polygon class="offer-panel" points="912,0 1200,0 1200,148 872,148" fill="var(--brand-green)"/>
    </svg>

    <div class="brand">
      <span class="brand__mark"></span>
      <span class="brand__name">
        <span class="brand__name-main">HARBOR PEAK</span>
        <span class="brand__name-sub">LOANS, LLC</span>
      </span>
    </div>

    <div class="offer">
      <p>Ask about our<br>"No Credit Score"<br>program for KSV and TQ</p>
    </div>
  </div>
</body>
</html>
```